Marcus Delvane Wellness podcast

I have overcome many health challenges. All of them have put me in position to help other people do the same. Eventually I became a certified health coach through the Academy of Restorative Dietetics. I have a strong desire to help because I know what it’s like to not feel well, and do what you want. The content on this sight will equip you with the tools to live a life full of health, freedom, and happiness. Complex health topics are broken down into simple ways to understand. No wellness topic is off limits, whether its heart disease, cancer, diabetes, sleep, hormones, or any other wellness topic.

Target Market(s)

People who are interested in growth and getting healthier

Industry/Entity Type

Health and Wellness

Colors
0054AA
0677BA
7BADD7
CADEEF
E8F1F8
0094D4
00A9DD
6FCCEA
C7EBF8
E9F6FB

Requirements
Must have
• None
Nice to have
• None
Should not have
• None

```html
<!DOCTYPE html>
<html lang="en">
<head>
<meta charset="utf-8">
<title>Marcus Delvane Wellness podcast</title>
<link rel="stylesheet" href="https://fonts.googleapis.com/css2?family=Montserrat:wght@400;700&family=Great+Vibes&display=swap">
<style>
  :root {
    --brand-blue: #0054AA;
    --accent-blue: #0094D4;
    --white: #FFFFFF;
    --photo-green: #5f7a4a;
    --photo-earth: #8a5a3a;
  }
  html, body {
    margin: 0;
    padding: 0;
    width: 1200px;
    height: 1200px;
    overflow: hidden;
    background: var(--white);
  }
  .cover {
    position: relative;
    width: 1200px;
    height: 1200px;
    overflow: hidden;
    background: var(--brand-blue);
  }
  .cover-art {
    position: absolute;
    inset: 0;
    width: 1200px;
    height: 1200px;
  }
  .frame {
    position: absolute;
    left: 56px;
    top: 56px;
    width: 1076px;
    height: 1076px;
    border: 9px solid var(--white);
    box-sizing: border-box;
  }
  .host-name {
    position: absolute;
    left: 92px;
    top: 268px;
    margin: 0;
    font-family: "Montserrat", sans-serif;
    font-weight: 700;
    font-size: 104px;
    line-height: 108px;
    color: var(--white);
    letter-spacing: 0.5px;
  }
  .show-type {
    position: absolute;
    left: 98px;
    top: 606px;
    margin: 0;
    font-family: "Montserrat", sans-serif;
    font-weight: 400;
    font-size: 54px;
    color: var(--white);
    letter-spacing: 1px;
  }
  .tagline {
    position: absolute;
    left: 106px;
    top: 812px;
    margin: 0;
    font-family: "Great Vibes", cursive;
    font-size: 64px;
    color: var(--white);
  }
</style>
</head>
<body>
  <main class="cover">
    <svg class="cover-art" viewBox="0 0 1200 1200" xmlns="http://www.w3.org/2000/svg">
      <defs>
        <linearGradient id="photo-tones" x1="0" y1="0" x2="0" y2="1">
          <stop offset="0" stop-color="#6f8f58"/>
          <stop offset="0.45" stop-color="#4f6b3c"/>
          <stop offset="0.6" stop-color="#a07a55"/>
          <stop offset="1" stop-color="#7a4e33"/>
        </linearGradient>
      </defs>
      <polygon class="host-photo" points="900,0 1200,0 1200,1200 460,1200"
               fill="url(#photo-tones)" role="img"
               aria-label="Photo of the host smiling in a white T-shirt, standing among pine trees in a forest clearing"/>
      <polygon class="accent-stripe" points="884,0 900,0 460,1200 444,1200" fill="var(--accent-blue)"/>
    </svg>
    <div class="frame"></div>
    <h1 class="host-name">Marcus<br>Delvane</h1>
    <p class="show-type">Wellness podcast</p>
    <p class="tagline">Feel great every day</p>
  </main>
</body>
</html>
```